Carwash Signage

We own and operate a 25m tunnel car wash in the uk. We are looking to upgrade our signage to include the following:-

Wash selection Board Size-1300x1300mm
Conditions 1300x1300mm
Instructions 1300x1300mm
Banner 2600x600mm
Stamp card flyer a5 double sided - 9 squares for stamping 3rd square needs to say free air freshener 9th square needs to say free vip car wash.

I have attached some notes for the details that are required to be included.

We are looking for a modern smart look more European car wash style than American car wash style. It should be bold and clear. with yellow/orange & blue/green,grey colours

The final design must be in a industry standard printable format.

UPDATED BRIEF AS DISCUSSED: We require design for 2 x window decals, flag design and 50% off voucher. Attached are rough layout drawings of what they should look like - we expect the designs to be in keeping with the previous designs colours, etc that have been carried out. We Look forward to hearing from you.

Target Market(s)

local car owners within a 15-20 mile radius

Colors
0054AA
0677BA
7BADD7
CADEEF
E8F1F8
0094D4
00A9DD
6FCCEA
C7EBF8
E9F6FB
00AB8E
00BBA5
67D7C9
C6EFE9
E9F9F6

Requirements
Must have
• must be sharp and modern European look

```html
<!DOCTYPE html>
<html lang="en">
<head>
<meta charset="utf-8">
<title>Silverton Car Wash – Banner</title>
<link href="https://fonts.googleapis.com/css2?family=Montserrat:wght@800;900&family=Open+Sans:wght@400;600;700;800&display=swap" rel="stylesheet">
<style>
  :root {
    --brand-blue: #0d3bc2;
    --deep-blue: #0a2fb0;
    --badge-blue: #1e8fe6;
    --pill-blue: #1a7ee8;
    --icon-blue: #2a8be8;
    --ink-grey: #3c3c3c;
    --panel-dark: rgba(40, 40, 44, 0.86);
    --white: #ffffff;
    --photo-light: #c9dfeb;
    --photo-mid: #9fc3da;
    --photo-base: #2a44cc;
  }
  * { margin: 0; padding: 0; box-sizing: border-box; }
  html, body { width: 1200px; height: 457px; overflow: hidden; background: #e2e2e2; }
  .banner {
    position: relative; width: 1200px; height: 457px; overflow: hidden;
    font-family: "Open Sans", Arial, sans-serif;
  }
  .tunnel-backdrop {
    position: absolute; inset: 0;
    background: radial-gradient(ellipse at 50% 40%, #f0f0f0 0%, #d4d4d4 50%, #b0b0b0 100%);
  }
  .attended {
    position: absolute; left: 32px; top: 22px;
    font-weight: 700; font-size: 29px; letter-spacing: -0.3px;
    color: var(--deep-blue); text-decoration: underline; text-decoration-thickness: 2px;
    text-underline-offset: 3px;
  }
  .brand-mark {
    position: absolute; left: 992px; top: 38px;
    display: flex; align-items: center; gap: 8px;
  }
  .brand-mark .dot { width: 24px; height: 24px; border-radius: 50%; background: var(--deep-blue); }
  .brand-mark .name { font-weight: 800; font-size: 22px; color: var(--deep-blue); letter-spacing: 0.5px; }
  .headline-place {
    position: absolute; left: 0; width: 1252px; top: 54px; text-align: center;
    font-weight: 700; font-size: 56px; line-height: 60px; color: var(--ink-grey); letter-spacing: 1px;
    text-shadow: 0 3px 6px rgba(0,0,0,0.25);
  }
  .headline-service {
    position: absolute; left: 0; width: 1240px; top: 104px; text-align: center;
    font-family: "Montserrat", Arial, sans-serif; font-weight: 900; font-size: 98px; line-height: 100px;
    color: var(--brand-blue); letter-spacing: -3px;
    text-shadow: 0 5px 10px rgba(0,0,40,0.4);
  }
  .car-photo {
    position: absolute; left: 346px; top: 196px; width: 609px; height: 225px;
    background: linear-gradient(180deg, var(--photo-light) 0%, var(--photo-mid) 65%, var(--photo-base) 100%);
  }
  .offer-badge {
    position: absolute; left: 877px; top: 203px; width: 102px; height: 102px;
    border-radius: 50%; background: var(--badge-blue);
    box-shadow: 0 0 0 3px rgba(255,255,255,0.9), 0 4px 10px rgba(0,0,0,0.3);
    color: var(--white); text-align: center; font-weight: 700;
    display: flex; flex-direction: column; justify-content: center; line-height: 1.05;
  }
  .offer-badge .small { font-size: 16px; }
  .offer-badge .big { font-size: 23px; font-weight: 800; }
  .info-panel {
    position: absolute; background: var(--panel-dark); border-radius: 9px;
    color: var(--white); box-shadow: 0 3px 8px rgba(0,0,0,0.25);
  }
  .hours { left: 50px; top: 272px; width: 140px; height: 76px; }
  .payment { left: 1010px; top: 272px; width: 139px; height: 100px; }
  .pill {
    position: absolute; background: var(--pill-blue); border-radius: 10px;
    font-weight: 600; color: var(--white); white-space: nowrap;
  }
  .hours .pill { left: 8px; top: 8px; width: 125px; height: 18px; font-size: 12px; padding-left: 27px; line-height: 18px; }
  .hours .pill svg { position: absolute; left: 4px; top: -4px; }
  .hours .row { position: absolute; left: 8px; font-size: 11.5px; display: flex; }
  .hours .row .day { width: 66px; }
  .payment .pill { left: 6px; top: 13px; height: 17px; font-size: 10px; padding: 0 7px; line-height: 17px; }
  .payment .method { position: absolute; left: 12px; display: flex; align-items: center; gap: 8px; font-size: 12px; }
</style>
</head>
<body>
<div class="banner">
  <div class="tunnel-backdrop" role="img" aria-label="Soft grey photograph of a foam-filled car wash tunnel"></div>

  <div class="attended">ATTENDED</div>

  <div class="brand-mark">
    <span class="dot"></span>
    <span class="name">SILVERTON</span>
  </div>

  <div class="headline-place">SILVERTON</div>
  <div class="headline-service">CAR WASH</div>

  <div class="car-photo" role="img" aria-label="Photograph of a light blue sports coupe in side view on a blue display podium"></div>

  <div class="offer-badge">
    <span class="small">9 washes/</span>
    <span class="small">FREE VIP</span>
    <span class="big">Wash!</span>
  </div>

  <div class="info-panel hours">
    <div class="pill">
      <svg width="22" height="22" viewBox="0 0 22 22" aria-hidden="true">
        <rect x="3" y="6" width="16" height="13" rx="1.5" fill="none" stroke="#fff" stroke-width="1.4"/>
        <line x1="3" y1="10" x2="19" y2="10" stroke="#fff" stroke-width="1.2"/>
        <circle cx="8" cy="6" r="4.5" fill="#1a7ee8" stroke="#fff" stroke-width="1.3"/>
        <path d="M8 4v2.2l1.5 1" stroke="#fff" stroke-width="1.1" fill="none"/>
      </svg>
      OPENING TIME
    </div>
    <div class="row" style="top:34px"><span class="day">MON-SAT :</span><span>8:00-18:00</span></div>
    <div class="row" style="top:52px"><span class="day">SUN :</span><span>9:00 -18:00</span></div>
  </div>

  <div class="info-panel payment">
    <div class="pill">PAYMENT OPTIONS</div>
    <div class="method" style="top:40px">
      <svg width="26" height="16" viewBox="0 0 26 16" aria-hidden="true">
        <rect x="1" y="1.5" width="24" height="13" rx="2" fill="none" stroke="var(--icon-blue)" stroke-width="1.4"/>
        <circle cx="13" cy="8" r="3.5" fill="none" stroke="var(--icon-blue)" stroke-width="1.3"/>
      </svg>
      Card
    </div>
    <div class="method" style="top:67px">
      <svg width="26" height="18" viewBox="0 0 26 18" aria-hidden="true">
        <rect x="1" y="1.5" width="24" height="15" rx="2" fill="none" stroke="var(--icon-blue)" stroke-width="1.4"/>
        <line x1="1" y1="6" x2="25" y2="6" stroke="var(--icon-blue)" stroke-width="1.4"/>
        <line x1="5" y1="11" x2="12" y2="11" stroke="var(--icon-blue)" stroke-width="1.3"/>
      </svg>
      Cash Accepted
    </div>
  </div>
</div>
</body>
</html>
```